Long Established Local Fencing (not swords) Business needs fresh Business Cards

We need fresh double sided business cards for our Fencing Construction business, we are looking for something with our new logo design added, and maybe a photo background ?
We recently had cards made from Cardlyne and we were horrified with what we got back, the quality was terrible, so am looking for high quality format for good printing company to make.
We install Steelmora, Timber paling, Aluminium Slat Screening, Picket (timber and aluminium) and most other fencing installations.
Our website is brankelrails.com.au should you like to learn a bit more.
We do have logo in other formats if required.
We have been in business for over 35 years and we have used this as a "motto" it is on our signage

Industry/Entity Type

Construction

Contact Information for Business Card

Open to ideas, we need 3 x different cards, one generic with no name and 2 x others each with 1 of our bosses name on each, I will put into upload files.

Colors
ec1f27
000000
606060
f5f5f5

Requirements
Must have
• Company Name and Logo
• Address
• Contact details, phone, website, email etc
• Small space to write notes when leaving card at residence
Nice to have
• Our motto "Servicing the Peninsula for over 35 years"

```html
<!DOCTYPE html>
<html lang="en">
<head>
<meta charset="utf-8">
<title>Brankel Rails – Business Cards</title>
<link rel="stylesheet" href="https://fonts.googleapis.com/css2?family=Exo+2:wght@300;400;700;800&display=swap">
<style>
  :root{
    --red:#ec1f27;
    --black:#000000;
    --grey:#606060;
    --paper:#ffffff;
    --stage:#d0d1d3;
    --stage-dark:#87888c;
    --photo-a:#3d4f3a;
    --photo-b:#2c3b5e;
  }
  html,body{margin:0;padding:0;overflow:hidden;}
  body{width:1200px;height:1200px;position:relative;background:var(--stage);font-family:"Exo 2",sans-serif;}
  .stage-band{position:absolute;inset:0;}
  .card{position:absolute;width:506px;height:289px;box-shadow:2px 4px 6px rgba(0,0,0,.35);background:var(--paper);}
  .card svg{display:block;width:100%;height:100%;}
  .card--front-a{left:61px;top:74px;}
  .card--lewis{left:618px;top:74px;}
  .card--generic{left:61px;top:406px;}
  .card--dean{left:618px;top:406px;}
  .card--front-back{left:386px;top:829px;}
  .card--front-top{left:225px;top:770px;}
  .t-light{font-family:"Exo 2",sans-serif;font-weight:300;}
  .t-body{font-family:"Exo 2",sans-serif;font-weight:400;fill:var(--black);}
  .t-heavy{font-family:"Exo 2",sans-serif;font-weight:800;}
  .brand{font-family:"Exo 2",sans-serif;font-weight:800;fill:var(--black);text-anchor:middle;}
  .red{fill:var(--red);}
  .blk{fill:var(--black);}
</style>
</head>
<body>

<svg class="stage-band" viewBox="0 0 1200 1200" aria-hidden="true">
  <polygon points="0,1120 1200,837 1200,1200 0,1200" fill="var(--stage-dark)"/>
</svg>

<svg width="0" height="0" style="position:absolute">
  <defs>
    <linearGradient id="photoGate" x1="0" y1="0" x2="0" y2="1">
      <stop offset="0" stop-color="#b9a58a"/><stop offset=".5" stop-color="#3f5a3b"/><stop offset="1" stop-color="#2f3b2c"/>
    </linearGradient>
    <linearGradient id="photoPanel" x1="0" y1="0" x2="0" y2="1">
      <stop offset="0" stop-color="#a7b3c4"/><stop offset=".35" stop-color="#2c3b5e"/><stop offset="1" stop-color="#243049"/>
    </linearGradient>
    <linearGradient id="photoLane" x1="0" y1="0" x2="0" y2="1">
      <stop offset="0" stop-color="#8fa07a"/><stop offset=".55" stop-color="#3d5236"/><stop offset="1" stop-color="#8a8a86"/>
    </linearGradient>
    <g id="frontFace">
      <rect width="607" height="347" fill="var(--paper)"/>
      <polygon points="523,0 607,0 607,135" class="blk"/>
      <polygon points="565,183 607,105 607,183" class="red"/>
      <rect x="0" y="183" width="198" height="132" fill="url(#photoGate)" role="img" aria-label="Photo of a steel garden gate with hedge"/>
      <rect x="203" y="183" width="198" height="132" fill="url(#photoPanel)" role="img" aria-label="Photo of a blue steel panel fence in front of a house"/>
      <rect x="407" y="183" width="200" height="132" fill="url(#photoLane)" role="img" aria-label="Photo of a tubular fence along a driveway"/>
      <polygon points="0,315 120,315 140,347 0,347" class="red"/>
      <polygon points="495,315 607,315 607,347 478,347" class="red"/>
      <text x="294" y="337" text-anchor="middle" class="t-body" font-size="16" letter-spacing="2.4">www.brankelrails.com.au</text>
      <circle cx="115" cy="58" r="24" class="red"/>
      <text x="115" y="124" class="brand" font-size="29">BRANKEL</text>
      <text x="115" y="156" class="brand" font-size="29">RAILS</text>
      <text x="258" y="70" class="t-light blk" font-size="25">SERVICING THE</text>
      <text x="275" y="100" class="t-heavy red" font-size="37">PENINSULA</text>
      <text x="256" y="123" class="t-light blk" font-size="25">FOR OVER</text>
      <text x="335" y="153" class="t-heavy red" font-size="37">35 YEARS</text>
    </g>
    <g id="iconPin"><path d="M0,-9 a7,7 0 0 1 7,7 c0,5 -7,12 -7,12 c0,0 -7,-7 -7,-12 a7,7 0 0 1 7,-7z M0,-5 a3,3 0 1 0 0.01,0z" class="red" fill-rule="evenodd"/></g>
    <g id="iconPhone"><path d="M6,-9 l3,4 l-3,3 c-3,2 -6,7 -6,10 l4,1 l1,4 c-6,1 -12,-3 -10,-10 c2,-7 6,-11 11,-12z" class="red"/></g>
    <g id="iconMail"><rect x="-8" y="-6" width="16" height="12" class="red"/><path d="M-8,-6 L0,1 L8,-6 M-8,6 L-2,0 M8,6 L2,0" stroke="#fff" stroke-width="1.4" fill="none"/></g>
    <g id="iconWeb"><circle r="8" class="red"/><path d="M-8,0 H8 M0,-8 V8 M-6,-4.5 H6 M-6,4.5 H6" stroke="#fff" stroke-width="1.2" fill="none"/><ellipse rx="3.5" ry="8" stroke="#fff" stroke-width="1.2" fill="none"/></g>
    <g id="iconMobile"><rect x="-6" y="-11" width="12" height="22" rx="2" class="red"/><rect x="-4" y="-8" width="8" height="6" fill="#fff"/><path d="M-3,1 h2 M1,1 h2 M-3,4 h2 M1,4 h2 M-3,7 h2 M1,7 h2" stroke="#fff" stroke-width="1.4"/></g>
    <g id="contactBlock">
      <use href="#iconPin" x="0" y="0"/>
      <text x="20" y="6" class="t-body" font-size="17">PO Box 218</text>
      <text x="20" y="30" class="t-body" font-size="17">Kelmar Bay NSW 2299</text>
      <use href="#iconPhone" x="0" y="66"/>
      <text x="20" y="73" class="t-body" font-size="17">(02) 5550 1184</text>
      <use href="#iconMail" x="0" y="90"/>
      <text x="20" y="96" class="t-body" font-size="16.5">office@brankelrails.com.au</text>
      <use href="#iconWeb" x="0" y="113"/>
      <text x="20" y="119" class="t-body" font-size="16.5">www.brankelrails.com.au</text>
    </g>
    <g id="backShapes">
      <rect width="607" height="347" fill="var(--paper)"/>
      <polygon points="0,0 113,0 0,145" class="red"/>
      <polygon points="0,145 50,145 25,108" class="blk"/>
      <polygon points="525,0 607,0 607,135" class="blk"/>
      <polygon points="480,347 607,110 607,347" class="red"/>
    </g>
    <g id="rightBrand">
      <circle cx="413" cy="62" r="24" class="red"/>
      <text x="413" y="136" class="brand" font-size="29">BRANKEL</text>
      <text x="413" y="168" class="brand" font-size="29">RAILS</text>
    </g>
  </defs>
</svg>

<div class="card card--front-a">
  <svg viewBox="0 0 607 347"><use href="#frontFace"/></svg>
</div>

<div class="card card--lewis">
  <svg viewBox="0 0 607 347">
    <use href="#backShapes"/>
    <rect x="33" y="41" width="200" height="37" fill="var(--paper)"/>
    <text x="42" y="70" class="t-heavy" font-size="25"><tspan class="blk">LEWIS </tspan><tspan class="red">HARROW</tspan></text>
    <use href="#iconMobile" x="80" y="101"/>
    <text x="100" y="109" class="t-light blk" font-size="21">0400 555 218</text>
    <text x="68" y="134" class="t-body" font-size="16">LICENSE No. 40215K</text>
    <use href="#contactBlock" x="51" y="196"/>
    <use href="#rightBrand"/>
  </svg>
</div>

<div class="card card--generic">
  <svg viewBox="0 0 607 347">
    <use href="#backShapes"/>
    <use href="#rightBrand" y="4"/>
    <text x="413" y="202" text-anchor="middle" class="t-body" font-size="16">LICENSE No. 40215K</text>
    <use href="#contactBlock" x="51" y="196"/>
  </svg>
</div>

<div class="card card--dean">
  <svg viewBox="0 0 607 347">
    <use href="#backShapes"/>
    <rect x="33" y="41" width="230" height="37" fill="var(--paper)"/>
    <text x="42" y="70" class="t-heavy" font-size="25"><tspan class="blk">DEAN </tspan><tspan class="red">CORBETT</tspan></text>
    <use href="#iconMobile" x="80" y="101"/>
    <text x="100" y="109" class="t-light blk" font-size="21">0400 555 371</text>
    <text x="68" y="134" class="t-body" font-size="16">LICENSE No. 40215K</text>
    <use href="#contactBlock" x="51" y="196"/>
    <use href="#rightBrand"/>
  </svg>
</div>

<div class="card card--front-back">
  <svg viewBox="0 0 607 347"><use href="#frontFace"/></svg>
</div>

<div class="card card--front-top">
  <svg viewBox="0 0 607 347"><use href="#frontFace"/></svg>
</div>

</body>
</html>
```